Brindle's Business Card

I need some designs for a new business card including the new logo attached. An old example of our business card is also attached to show all the data that should be included on the new design.
**I added some more examples someone had mocked up**

Contact Information for Business Card

Should include all info on other examples uploaded.

```html
<!DOCTYPE html>
<html lang="en">
<head>
<meta charset="utf-8">
<title>Brindle's Business Card</title>
<link href="https://fonts.googleapis.com/css2?family=Montserrat:wght@500;600;700;800&display=swap" rel="stylesheet">
<style>
  :root {
    --brand-blue: #1a6fc0;
    --brand-red: #e3262d;
    --faint-blue: #dcebf8;
    --faint-red: #fbe1e2;
    --card: #ffffff;
    --stage: #eceae6;
  }
  * { box-sizing: border-box; margin: 0; padding: 0; }
  html, body { width: 1200px; height: 892px; overflow: hidden; }
  body {
    background: var(--stage);
    font-family: "Montserrat", Arial, sans-serif;
    display: flex;
    flex-direction: column;
    align-items: center;
    justify-content: center;
    gap: 40px;
  }
  .card {
    position: relative;
    width: 700px;
    height: 400px;
    background: var(--card);
    box-shadow: 0 6px 18px rgba(0,0,0,0.12);
    overflow: hidden;
  }
  .card--front, .card--back { height: 400px; }
  .card--front { width: 700px; }
  body { gap: 30px; }
  .card { width: 720px; height: 411px; }

  .brand { display: flex; align-items: center; gap: 14px; }
  .brand__dot {
    width: 58px; height: 58px; border-radius: 50%;
    background: var(--brand-red);
    flex: none;
  }
  .brand__text { display: flex; flex-direction: column; }
  .brand__name {
    color: var(--brand-blue);
    font-weight: 800;
    font-size: 62px;
    line-height: 1;
    letter-spacing: 1px;
  }
  .brand__tagline {
    color: var(--brand-red);
    font-weight: 600;
    font-size: 14.5px;
    letter-spacing: 0.6px;
    margin-top: 6px;
    text-transform: uppercase;
  }

  .decor-circle {
    position: absolute;
    border-radius: 50%;
    background: var(--faint-blue);
    opacity: 0.7;
  }

  /* front */
  .card--front .decor-circle { width: 330px; height: 330px; right: -40px; top: 70px; }
  .card--front .brand { position: absolute; left: 130px; top: 150px; z-index: 1; }

  /* back */
  .card--back .decor-circle { width: 360px; height: 360px; right: 60px; top: 140px; background: var(--faint-red); opacity: 0.6; }
  .card--back .brand { position: absolute; left: 44px; top: 34px; z-index: 1; }
  .card--back .brand__dot { width: 40px; height: 40px; }
  .card--back .brand__name { font-size: 42px; }
  .card--back .brand__tagline { font-size: 10px; }

  .contact { position: absolute; left: 44px; top: 138px; z-index: 1; color: var(--brand-blue); }
  .contact__row { display: flex; align-items: center; gap: 14px; margin-bottom: 14px; }
  .contact__icon { width: 22px; height: 22px; flex: none; fill: var(--brand-red); }
  .contact__name { font-weight: 700; font-size: 30px; }
  .contact__row--name .contact__icon { width: 30px; height: 30px; }
  .contact__text { font-weight: 500; font-size: 17px; line-height: 1.35; }
  .contact__row--address { align-items: flex-start; }

  .credentials {
    position: absolute; right: 44px; bottom: 34px; z-index: 1;
    color: var(--brand-blue); font-weight: 600; font-size: 20px;
    text-align: right; line-height: 1.3;
  }
</style>
</head>
<body>
  <section class="card card--front" aria-label="Card front">
    <div class="decor-circle" aria-hidden="true"></div>
    <div class="brand">
      <span class="brand__dot" aria-hidden="true"></span>
      <div class="brand__text">
        <span class="brand__name">BRINDLE'S</span>
        <span class="brand__tagline">Air Conditioning &amp; Heating Service</span>
      </div>
    </div>
  </section>

  <section class="card card--back" aria-label="Card back">
    <div class="decor-circle" aria-hidden="true"></div>
    <div class="brand">
      <span class="brand__dot" aria-hidden="true"></span>
      <div class="brand__text">
        <span class="brand__name">BRINDLE'S</span>
        <span class="brand__tagline">Air Conditioning &amp; Heating Service</span>
      </div>
    </div>

    <div class="contact">
      <div class="contact__row contact__row--name">
        <svg class="contact__icon" viewBox="0 0 24 24" aria-hidden="true"><circle cx="12" cy="7" r="5"/><path d="M2 23c0-6 4.5-9 10-9s10 3 10 9z"/></svg>
        <span class="contact__name">Dale Brindle</span>
      </div>
      <div class="contact__row">
        <svg class="contact__icon" viewBox="0 0 24 24" aria-hidden="true"><path d="M2 5h20v14H2z" fill="none"/><path d="M2 5h20L12 13z"/><path d="M2 7l10 8 10-8v12H2z"/></svg>
        <span class="contact__text">service@brindlehvac.net</span>
      </div>
      <div class="contact__row">
        <svg class="contact__icon" viewBox="0 0 24 24" aria-hidden="true"><path d="M6.6 10.8a15 15 0 0 0 6.6 6.6l2.2-2.2a1 1 0 0 1 1-.25 11.4 11.4 0 0 0 3.6.57 1 1 0 0 1 1 1V20a1 1 0 0 1-1 1A17 17 0 0 1 3 4a1 1 0 0 1 1-1h3.5a1 1 0 0 1 1 1c0 1.25.2 2.45.57 3.57a1 1 0 0 1-.25 1z"/></svg>
        <span class="contact__text">555-014-2273</span>
      </div>
      <div class="contact__row contact__row--address">
        <svg class="contact__icon" viewBox="0 0 24 24" aria-hidden="true"><path d="M12 2a7 7 0 0 0-7 7c0 5 7 13 7 13s7-8 7-13a7 7 0 0 0-7-7zm0 9.5A2.5 2.5 0 1 1 12 6.5a2.5 2.5 0 0 1 0 5z"/></svg>
        <span class="contact__text">418 Alder Lane<br>Maple Falls, IA 50012 USA</span>
      </div>
    </div>

    <p class="credentials">Licensed &amp; Insured<br>Family Owned &amp; Operated</p>
  </section>
</body>
</html>
```